MARLO Real Estate Prospecting DL Flyer

I need a DL size (99mm x 210mm) two sided flyer designed for letter boxing and also handing to prospective clients when door knocking across my sales area in Melbourne, Australia. PLEASE NOTE: the flyer is a flat flyer to be designed on both sides as per my doc below. The flyer will likely be printed on 350gsm card. It will not be posted - so NO space for address required. It is for door-knocking (door to door sales) and letter boxing (dropped personally by me in a letterbox - not posted).
My original company logo design brief was that it should be modern and premium black on white and white on black - drawing influences by FELIX DORNE and also CALISTA. I want my DL flyer to reflect the same influence. I have attached proposed copy on the word document attached below.
The DL flyer will be printed on 350 gsm - probably gloss to reflect the premium feel, but open to suggestion. It is important for the flyer to be durable and have decent shelf life - I am not going for cheap and cheerful on this project. I need to make an impact. I am trying to attract home owners to my business to list and sell their properties - usually for most people their biggest asset is their home/property - so it is important that my business is credible and very experienced (which of course it is).
For a view of the types of properties I sell please go to www.homelistingsdemo.com.au and type in Mount Waverley, Victoria; and also Glen Waverley, Victoria. You will see a list of properties come up that are either for SALE or for SALE BY AUCTION. This may help with your understanding. The areas I concentrate on are very suburban - meaning families, families, families :)

Target Market(s)

Property owners across the middle ring of eastern suburbs of Melbourne. Value of homes are between $1m and $2m, and mostly consist of 3 and 4 bedroom family homes. Clients range from the elderly looking to downsize to a smaller property, to families looking to sell and upgrade their homes.

Industry/Entity Type

Real Estate Agent

Font styles to use
Serif

Colors
000000
ffffff

Requirements
Must have
• The "call to action" components that I have included on the doc file and include a FREE E-BOOK on supply of their contact details; and a FREE PROFESSIONAL HOME STYLIST CONSULTATION.
• It must feature my company logo. My corporate colours are black and white - so best to stick with these in the design.
• UPDATE: Just call the e-book "5 EASY STEPS TO LIFT THE FINAL OFFER ON YOUR HOUSE"
• ...forget the City of Brellton and City of Parkvane part!!
• UPDATE: Designs I have liked the best include the following elements:
• 1. Strong brand at top of each side of flyer
• 2. Family pic page 1; property pic page 2
• 3. BOLD Headings
• 4. Amplified CALL TO ACTION - FREE......consult; FREE E-Book
• 5. Clear visible contact details at bottom of page
Nice to have
• Lifestyle photography of homes.
• Some designers have used Asian families in their pics - which is smart as the main buyer demographic is Chinese families. The mail ownership is Australian - so a mix of Asian and Anglo is fine. Try and avoid overtly USA style properties - as Melbourne styles are different. Keys, handshakes etc are all good :)
Should not have
• Animation, cartoons, or visual drawings included.

```html
<!DOCTYPE html>
<html lang="en">
<head>
<meta charset="utf-8">
<title>MARLO Real Estate – DL Flyer</title>
<link rel="stylesheet" href="https://fonts.googleapis.com/css2?family=Lato:wght@300;400;700;900&display=swap">
<style>
  :root{
    --black:#000000;
    --white:#ffffff;
    --ink:#1a1a1a;
    --mid:#555555;
    --soft:#cfcfcf;
    --stage:#e6e6e6;
  }
  *{box-sizing:border-box;margin:0;padding:0}
  html,body{width:1147px;height:1200px;overflow:hidden}
  body{background:var(--stage);font-family:'Lato',sans-serif;position:relative}
  .flyer{position:absolute;overflow:hidden;box-shadow:0 3px 10px rgba(0,0,0,.25)}
  .abs{position:absolute}
  .front-headline,.front-intro,.front-offer,.front-brand{z-index:2}

  /* Front side */
  .front{left:128px;top:144px;width:432px;height:918px;
    background:linear-gradient(180deg,#979797 0%,#c9c9c9 20%,#f7f7f7 38%,#ffffff 50%)}
  .front-headline{left:0;width:432px;top:48px;text-align:center;font-weight:300;
    font-size:53px;line-height:44px;color:var(--ink);letter-spacing:-.5px}
  .front-intro{left:36px;top:198px;font-weight:300;font-size:17px;line-height:21.5px;color:#2a2a2a}
  .front-intro b{font-weight:700;color:var(--ink)}
  .agent-photo{left:200px;top:356px;width:232px;height:510px;z-index:1;
    background:linear-gradient(180deg,#e9e9e9 0%,#d2d2d2 28%,#f4f4f4 34%,#2b2b2b 46%,#111 100%);
    border-radius:116px 0 0 0}
  .front-offer{left:36px;top:496px;font-weight:700;font-size:21.5px;line-height:24.5px;color:var(--mid)}
  .front-offer span{color:var(--black)}
  .front-brand{left:40px;top:770px;width:140px;text-align:center}
  .brand-name{font-weight:700;color:var(--black);letter-spacing:1px;line-height:1}
  .front-brand .brand-name{font-size:37px;letter-spacing:0}
  .brand-tag{font-weight:400;text-transform:uppercase;white-space:nowrap}
  .front-brand .brand-tag{font-size:7.5px;letter-spacing:6.5px;color:#333;margin-top:5px;margin-right:-6.5px}
  .contact-bar{left:0;width:100%;height:52px;background:var(--black);color:var(--white);z-index:3;
    font-weight:700;font-size:16px;display:flex;align-items:center;justify-content:center;gap:10px}
  .front .contact-bar{top:866px}

  /* Back side */
  .back{left:606px;top:145px;width:434px;height:921px;
    background:linear-gradient(180deg,#000 0%,#000 40%,#3a3a3a 56%,#8a8a8a 70%,#bdbdbd 80%,#d8d8d8 94%)}
  .back-brand{left:0;width:434px;top:36px;text-align:center}
  .back-brand .brand-name{font-size:90px;color:var(--white);letter-spacing:2px}
  .back-brand .brand-tag{font-size:14px;letter-spacing:23px;color:var(--white);margin-top:8px;margin-right:-23px}
  .property-photo{left:0;top:178px;width:205px;height:169px;
    background:linear-gradient(135deg,#c98a46 0%,#9c6b3e 35%,#d9dde2 65%,#aab3bd 100%)}
  .back-headline{left:208px;width:222px;top:170px;text-align:center;color:var(--white);
    font-weight:300;font-size:40px;line-height:35px}
  .back-pitch{left:40px;width:354px;top:366px;text-align:center;color:var(--soft);
    font-weight:700;font-size:16.5px;line-height:20px}
  .benefits{left:44px;top:526px;width:360px;list-style:none;color:var(--white);
    font-weight:300;font-size:17px;line-height:21px}
  .benefits li{position:relative;padding-left:18px;margin-bottom:4px}
  .benefits li::before{content:"";position:absolute;left:0;top:9px;width:6px;height:6px;border-radius:50%;background:var(--white)}
  .benefits b{font-weight:700}
  .benefits sup{font-size:10px}
  .ebook-glow{left:168px;top:660px;width:340px;height:340px;border-radius:50%;
    background:radial-gradient(circle,#ffffff 0%,#ffffff 55%,rgba(255,255,255,.6) 72%,rgba(255,255,255,0) 100%)}
  .ebook-cover{left:54px;top:688px;width:108px;height:160px;
    background:linear-gradient(180deg,#3a3a3a 0%,#5a5a5a 45%,#8b6a5c 70%,#2a2a2a 100%);
    box-shadow:4px 4px 8px rgba(0,0,0,.35)}
  .ebook-offer{left:170px;width:270px;top:697px;text-align:center;color:var(--ink)}
  .ebook-lead{font-weight:300;font-size:16px;line-height:17px}
  .ebook-lead b{font-weight:700}
  .ebook-title{font-weight:900;font-size:20.5px;line-height:19px;margin-top:10px}
  .ebook-title .num{font-size:42px;vertical-align:-4px}
  .ebook-action{font-weight:700;font-size:15.5px;margin-top:14px}
  .back .contact-bar{top:869px}
</style>
</head>
<body>

<section class="flyer front" aria-label="Flyer front">
  <h1 class="abs front-headline">A Decade<br>of Experience<br>on your Side</h1>
  <div class="abs agent-photo" role="img" aria-label="Portrait of the agent in a dark suit and striped tie"></div>
  <p class="abs front-intro">My name’s <b>Daniel Marlo</b>. With over a decade<br>of experience in the property industry I know<br>what it takes to get you the BEST POSSIBLE<br>PRICE for your property. I’ve spent much<br>of my career in the cutthroat world of<br>commercial property and closing high<br>stakes international real estate<br>deals. But 3 years ago I brought<br>my expertise home to focus on<br>the communities in Melbourne’s<br>eastern suburbs. I’ve had many<br>incredible sales results to date.<br>Will yours be next?</p>
  <p class="abs front-offer">Claim your <span>free<br>property market<br>appraisal</span> now<br>and receive<br><span>a bonus</span><br>professional<br>home stylist<br>consultation<br><span>– normally<br>worth $118</span></p>
  <div class="abs front-brand">
    <div class="brand-name">MARLO</div>
    <div class="brand-tag">Real Estate</div>
  </div>
  <div class="abs contact-bar"><span>P. 1800 555 019</span><span>E. sales@marlorealestate.com.au</span></div>
</section>

<section class="flyer back" aria-label="Flyer back">
  <div class="abs back-brand">
    <div class="brand-name">MARLO</div>
    <div class="brand-tag">Real Estate</div>
  </div>
  <div class="abs property-photo" role="img" aria-label="Bright open-plan kitchen and dining room with timber cabinets"></div>
  <h2 class="abs back-headline">Get the<br>Maximum<br>Price<br>for your<br>Property</h2>
  <p class="abs back-pitch">At MARLO Real Estate we are doing things differently. Our property sales process is designed to extract an ELITE LEVEL PRICE for you, but our cost of doing business is significantly reduced from that of our competitors, and that results in MORE MONEY IN YOUR POCKET.</p>
  <ul class="abs benefits">
    <li><b>ELITE</b> sales process ensures the<br>maximum possible price for your property.</li>
    <li>Low <b>FLATRATE FEE</b> <sup>TM</sup> selling commission –<br>up to half that charged by other agents.</li>
    <li>A <b>FLATRATE FEE</b> <sup>TM</sup> in high impact<br>marketing for the sale of your home.</li>
  </ul>
  <div class="abs ebook-glow"></div>
  <div class="abs ebook-cover" role="img" aria-label="E-book cover showing a house at dusk"></div>
  <div class="abs ebook-offer">
    <p class="ebook-lead">Get your <b>free</b><br>copy of my e-book:</p>
    <p class="ebook-title"><span class="num">5</span> Easy Steps<br>to Lift the<br>Final Offer on<br>your House</p>
    <p class="ebook-action">Just call or email:</p>
  </div>
  <div class="abs contact-bar"><span>P. 1800 555 019</span><span>E. sales@marlorealestate.com.au</span></div>
</section>

</body>
</html>
```